Loom Haven needs a website

I sell rugs and carpet on my website, loomhavenfloors.example. I need help with the site design to make it "pop". The logo in the header has been designed and I want the site to match it's style and color. Also I have some example sites for layout:
matvale.example
weave-outlet.example

Industry/Entity Type

Carpet

Requirements
Must have
• Scrolling images on front page. I will insert photos, just need the code.

```html
<!DOCTYPE html>
<html lang="en">
<head>
<meta charset="utf-8">
<title>Loom Haven — Carpet Flooring</title>
<link rel="stylesheet" href="https://fonts.googleapis.com/css2?family=Comfortaa:wght@400;700&family=Arimo:wght@400;700&family=Tinos:wght@700&family=Montserrat:wght@400;600&display=swap">
<style>
:root{
  --page-bg:#e9e9e9;
  --sheet:#ffffff;
  --brand-blue:#0d6fb8;
  --navy:#1b2f6b;
  --green:#6ab446;
  --green-dark:#3f8f2a;
  --text:#222222;
  --muted:#555555;
  --frame:#dddddd;
}
*{box-sizing:border-box;margin:0;padding:0}
html,body{width:989px;height:1200px;overflow:hidden}
body{background:var(--page-bg);font-family:Arimo,Arial,sans-serif;color:var(--text);position:relative}
.top-bar{position:absolute;left:0;top:0;width:989px;height:5px;background:#6d6d6d}
.bottom-bar{position:absolute;left:0;top:1194px;width:989px;height:6px;background:#6d6d6d}
.sheet{position:absolute;left:75px;top:5px;width:839px;height:1189px;background:var(--sheet)}
.abs{position:absolute}
a{color:inherit;text-decoration:none}

/* header */
.brand{left:92px;top:28px;display:flex;align-items:center;gap:10px;font-family:Comfortaa,sans-serif;font-size:30px;color:var(--navy);font-weight:400}
.brand-mark{width:26px;height:26px;border-radius:50%;background:var(--navy)}
.util-links{right:96px;top:26px;font-size:10.5px;color:#333}
.util-links .checkout{color:var(--brand-blue)}
.search{left:657px;top:68px;width:176px;height:26px;border:1px dotted #aaa;display:flex;align-items:center;justify-content:space-between;padding-left:9px;font-size:10px;color:#999}
.search-btn{width:20px;height:20px;background:var(--navy);margin-right:2px;display:flex;align-items:center;justify-content:center}
.cart{left:842px;top:74px;font-size:11px;color:#333;display:flex;align-items:center;gap:6px}
.cart-count{background:var(--navy);color:#fff;font-size:10px;width:25px;height:15px;text-align:center;line-height:15px;border-radius:2px}
.dotted{height:3px;background:repeating-linear-gradient(90deg,#c9c9c9 0 1px,transparent 1px 3px)}
.nav{left:92px;top:107px;display:flex;font-size:12px;color:#222;letter-spacing:.2px}
.nav a{display:block;padding:9px 0 10px;margin-right:47px;position:relative}
.nav a.active{padding-left:19px;padding-right:19px;margin-right:31px;border-bottom:3px solid var(--brand-blue)}

/* hero */
.hero{left:84px;top:142px;width:820px;height:289px;background:linear-gradient(100deg,#f2f2f2 0%,#ece9e4 35%,#d8c3a0 55%,#c49a63 70%,#a98253 82%,#6a2530 100%)}
.hero-shadow{left:110px;top:430px;width:790px;height:10px;background:radial-gradient(ellipse at top,rgba(0,0,0,.28),rgba(0,0,0,0) 70%)}
.hero-kicker{left:83px;top:182px;width:287px;height:43px;background:var(--green);color:#fff;font-family:Comfortaa,sans-serif;font-size:30px;padding-left:23px;line-height:43px}
.hero-title{left:83px;top:227px;width:411px;height:43px;background:var(--navy);color:#fff;font-family:Comfortaa,sans-serif;font-weight:700;font-size:34px;padding-left:22px;line-height:45px;letter-spacing:.3px}
.hero-copy{left:104px;top:286px;width:390px;font-size:11px;line-height:16.5px;color:#555}

/* welcome */
.welcome-title{left:91px;top:460px;font-family:Comfortaa,sans-serif;font-size:23px;color:var(--brand-blue)}
.welcome-title b{font-weight:700}
.welcome-copy{left:93px;top:502px;width:555px;font-size:11px;line-height:16.5px;color:#222}
.welcome-copy p+p{margin-top:16.5px}
.more{left:579px;top:628px;font-size:10px;font-style:italic;color:var(--brand-blue)}
.more span{color:#111;font-style:normal;font-weight:700}
.vsep{left:670px;top:468px;width:2px;height:162px;background:repeating-linear-gradient(180deg,#c9c9c9 0 1px,transparent 1px 3px)}
.cat-title{left:697px;top:464px;font-family:Comfortaa,sans-serif;font-size:19.5px;color:var(--brand-blue)}
.cat-list{left:698px;top:497px;width:156px;list-style:none;font-size:11.5px;color:#222}
.cat-list li{height:25px;line-height:24px;border-bottom:1px solid #ddd;padding-left:12px;position:relative}
.cat-list li:last-child{border-bottom:none}
.cat-list li::before{content:"";position:absolute;left:3px;top:11px;width:4px;height:4px;border-radius:50%;background:#666}

/* products */
.section-title{left:99px;top:668px;font-family:Tinos,serif;font-weight:700;font-size:20px;color:#555;letter-spacing:.3px}
.view-all{left:840px;top:677px;font-size:9.5px;color:#555;font-weight:700;display:flex;gap:7px;align-items:center}
.product{width:171px;height:224px;border:1px solid var(--frame);background:#fff;top:723px}
.product-img{position:absolute;left:8px;top:6px;width:154px;height:118px}
.wood{background:linear-gradient(120deg,#e3c07e,#d9b067 50%,#c99a50)}
.floral{background:radial-gradient(circle at 40% 40%,#a8aa86,#6b5a45 60%,#4b3b2d)}
.persian{background:radial-gradient(ellipse at center,#98977a,#7a5c3d 55%,#5a2b24)}
.product-name{position:absolute;left:9px;top:142px;font-size:9.5px;color:#666}
.price{position:absolute;left:10px;top:166px;font-family:Montserrat,sans-serif;font-weight:600;font-size:14px;color:var(--green-dark);letter-spacing:.5px}
.btns{position:absolute;left:10px;top:190px;display:flex;height:26px}
.buy{width:83px;background:linear-gradient(#5cb640,#36921f);color:#fff;font-size:9.5px;font-weight:700;display:flex;align-items:center;gap:6px;padding-left:7px}
.details{width:69px;background:linear-gradient(#f3f3f3,#dedede);color:#666;font-size:9.5px;font-weight:700;display:flex;align-items:center;gap:5px;padding-left:5px}

/* footer */
.foot-col{top:1005px;font-size:9.5px;color:#333}
.foot-col h4{font-family:Montserrat,sans-serif;font-weight:400;font-size:10px;letter-spacing:1.4px;color:#333;margin-bottom:13px;white-space:nowrap}
.foot-col.signup h4{font-size:9.5px;letter-spacing:.9px}
.foot-col li{list-style:none;height:23px}
.email{left:718px;top:1033px;width:171px;height:25px;border:1px solid #e2e2e2;font-size:8.5px;color:#888;padding:8px 6px}
.submit{left:819px;top:1065px;width:70px;height:23px;background:linear-gradient(#2f4f9e,#1b2f6b);color:#fff;font-family:Montserrat,sans-serif;font-size:11px;font-weight:600;letter-spacing:.8px;text-align:center;line-height:23px}
.social{left:739px;top:1112px;width:118px;display:flex;justify-content:space-between}
.social i{width:25px;height:25px;border-radius:50%;display:block}
.copyright{left:105px;top:1168px;font-size:11.5px;color:#222}
.pay{left:722px;top:1166px;width:165px;display:flex;gap:3px}
.pay span{flex:1 1 auto;height:19px;padding:0 2px;background:#eef1f7;border:1px solid #c8d0e0;font-size:7.5px;font-weight:700;color:var(--navy);line-height:17px;text-align:center;white-space:nowrap}
</style>
</head>
<body>
<div class="top-bar"></div>
<div class="sheet"></div>

<header>
  <div class="abs brand"><span class="brand-mark"></span>Loom Haven</div>
  <div class="abs util-links"><a href="#">My Account</a> &nbsp;|&nbsp; <a href="#">View Shopping Bag</a> &nbsp; (0 items ) &nbsp;| <a class="checkout" href="#">Go to Checkout</a></div>
  <div class="abs search">Search...
    <span class="search-btn"><svg width="13" height="13" viewBox="0 0 13 13"><circle cx="5.5" cy="5.5" r="4" fill="none" stroke="#fff" stroke-width="2"/><line x1="8.5" y1="8.5" x2="12" y2="12" stroke="#fff" stroke-width="2.2"/></svg></span>
  </div>
  <div class="abs cart">Cart <span class="cart-count">0</span></div>
  <div class="abs dotted" style="left:75px;top:106px;width:839px"></div>
  <nav class="abs nav">
    <a class="active" href="#">HOME</a><a href="#">ABOUT US</a><a href="#">CONTACT US</a><a href="#">MY ACCOUNT</a><a href="#">VIEW CART/CHECKOUT</a>
  </nav>
</header>

<section>
  <div class="abs hero" role="img" aria-label="Slideshow photo of rolled carpets in cream, tan and burgundy"></div>
  <div class="abs hero-shadow"></div>
  <div class="abs hero-kicker">loom haven</div>
  <div class="abs hero-title">CARPET FLOORING</div>
  <p class="abs hero-copy">simply dummy text of the printing and typesetting industry. Lorem Ipsum has been the industry's standard dummy text ever since the 1500s, when an unknown printer took a galley.</p>
</section>

<section>
  <h1 class="abs welcome-title"><b>Welcome to</b> loom haven</h1>
  <div class="abs welcome-copy">
    <p>Lorem Ipsum is simply dummy text of the printing and typesetting industry. Lorem Ipsum has been the industry's standard dummy text ever since the 1500s, when an unknown printer took a galley of type and scrambled it to make a type specimen book. It has survived not only five centuries, but also the leap into electronic typesetting, remaining essentially unchanged. It was popularised in the 1960s with</p>
    <p>The release of Typeset Co sheets containing Lorem Ipsum passages, and more recently with desktop publishing software like Pageform Studio including versions of Lorem Ipsum.</p>
  </div>
  <a class="abs more" href="#">More Details <span>»</span></a>
  <div class="abs vsep"></div>
  <h2 class="abs cat-title">Shop by Category</h2>
  <ul class="abs cat-list">
    <li>Commercial Flooring</li><li>Carpet Flooring</li><li>Harwood Flooring</li><li>Area Rugs</li><li>Carpet Flooring</li>
  </ul>
</section>

<section>
  <h2 class="abs section-title">Top Products</h2>
  <a class="abs view-all" href="#">VIEW ALL <svg width="7" height="8" viewBox="0 0 7 8"><path d="M0 0L7 4L0 8Z" fill="#0d6fb8"/></svg></a>
  <div class="abs dotted" style="left:98px;top:701px;width:798px"></div>

  <div class="abs product" style="left:98px">
    <div class="product-img wood" role="img" aria-label="Light oak hardwood flooring"></div>
    <div class="product-name">Golf Clubs - Silk Bow Tie</div><div class="price">$45.00</div>
    <div class="btns"><span class="buy"><svg width="16" height="12" viewBox="0 0 16 12"><path d="M0 1H3L5 8H13L15 3H4" fill="none" stroke="#fff" stroke-width="1.6"/><circle cx="6" cy="10.5" r="1.3" fill="#fff"/><circle cx="12" cy="10.5" r="1.3" fill="#fff"/></svg>BUY NOW</span><span class="details"><svg width="14" height="14" viewBox="0 0 14 14"><circle cx="5" cy="5" r="3.8" fill="none" stroke="#3f8f2a" stroke-width="1.8"/><line x1="8" y1="8" x2="13" y2="13" stroke="#3f8f2a" stroke-width="2.2"/></svg>DETAILS</span></div>
  </div>
  <div class="abs product" style="left:303px">
    <div class="product-img floral" role="img" aria-label="Brown floral area rug"></div>
    <div class="product-name">Golf Clubs - Silk Bow Tie</div><div class="price">$45.00</div>
    <div class="btns"><span class="buy"><svg width="16" height="12" viewBox="0 0 16 12"><path d="M0 1H3L5 8H13L15 3H4" fill="none" stroke="#fff" stroke-width="1.6"/><circle cx="6" cy="10.5" r="1.3" fill="#fff"/><circle cx="12" cy="10.5" r="1.3" fill="#fff"/></svg>BUY NOW</span><span class="details"><svg width="14" height="14" viewBox="0 0 14 14"><circle cx="5" cy="5" r="3.8" fill="none" stroke="#3f8f2a" stroke-width="1.8"/><line x1="8" y1="8" x2="13" y2="13" stroke="#3f8f2a" stroke-width="2.2"/></svg>DETAILS</span></div>
  </div>
  <div class="abs product" style="left:506px">
    <div class="product-img persian" role="img" aria-label="Traditional bordered rug in sage and rust"></div>
    <div class="product-name">Golf Clubs - Silk Bow Tie</div><div class="price">$45.00</div>
    <div class="btns"><span class="buy"><svg width="16" height="12" viewBox="0 0 16 12"><path d="M0 1H3L5 8H13L15 3H4" fill="none" stroke="#fff" stroke-width="1.6"/><circle cx="6" cy="10.5" r="1.3" fill="#fff"/><circle cx="12" cy="10.5" r="1.3" fill="#fff"/></svg>BUY NOW</span><span class="details"><svg width="14" height="14" viewBox="0 0 14 14"><circle cx="5" cy="5" r="3.8" fill="none" stroke="#3f8f2a" stroke-width="1.8"/><line x1="8" y1="8" x2="13" y2="13" stroke="#3f8f2a" stroke-width="2.2"/></svg>DETAILS</span></div>
  </div>
  <div class="abs product" style="left:712px">
    <div class="product-img floral" role="img" aria-label="Brown floral area rug"></div>
    <div class="product-name">Golf Clubs - Silk Bow Tie</div><div class="price">$45.00</div>
    <div class="btns"><span class="buy"><svg width="16" height="12" viewBox="0 0 16 12"><path d="M0 1H3L5 8H13L15 3H4" fill="none" stroke="#fff" stroke-width="1.6"/><circle cx="6" cy="10.5" r="1.3" fill="#fff"/><circle cx="12" cy="10.5" r="1.3" fill="#fff"/></svg>BUY NOW</span><span class="details"><svg width="14" height="14" viewBox="0 0 14 14"><circle cx="5" cy="5" r="3.8" fill="none" stroke="#3f8f2a" stroke-width="1.8"/><line x1="8" y1="8" x2="13" y2="13" stroke="#3f8f2a" stroke-width="2.2"/></svg>DETAILS</span></div>
  </div>
</section>

<footer>
  <div class="abs dotted" style="left:100px;top:985px;width:791px"></div>
  <div class="abs foot-col" style="left:100px"><h4>COMPANY INFO</h4><ul><li>Our Story</li><li>Press</li><li>Blog</li><li>Terms</li><li>Contact Us</li></ul></div>
  <div class="abs foot-col" style="left:263px"><h4>CUSTOMER CARE</h4><ul><li>Gift Cards</li><li>Size Charts</li><li>Find a Store</li><li>Contact Us</li><li>Custom Products</li></ul></div>
  <div class="abs foot-col" style="left:417px"><h4>MY ACCOUNT</h4><ul><li>Create an Account</li><li>Order Status</li><li>Wish List</li><li>Shipping</li><li>Returns</li></ul></div>
  <div class="abs foot-col" style="left:569px"><h4>COMPANY INFO</h4><ul><li>Our Story</li><li>Press</li><li>Blog</li><li>Terms</li><li>Contact Us</li></ul></div>
  <div class="abs foot-col signup" style="left:716px"><h4>SIGN-UP FOR OUR EMAIL LIST!</h4></div>
  <div class="abs email">Enter Your Email Here</div>
  <div class="abs submit">SUBMIT</div>
  <div class="abs dotted" style="left:716px;top:1097px;width:174px"></div>
  <div class="abs social" aria-label="Social links">
    <i style="background:#3b5998"></i>
    <i style="background:#2aa3dc"></i>
    <i style="background:#e0452f"></i>
    <i style="background:#f26b1d"></i>
  </div>
  <div class="abs dotted" style="left:100px;top:1153px;width:791px"></div>
  <p class="abs copyright">Copyright © 2010-2014 loom haven. All Rights Reserved.</p>
  <div class="abs pay"><span>PayNest</span><span>OrbitCard</span><span>Vistra</span><span>AmeriPass</span></div>
</footer>

<div class="bottom-bar"></div>
</body>
</html>
```